WordPress website in children books redesign

We are personalised children storybook creators with a range of personalized books, music CDs and DVDs that are created for each child. We sell our concept through a license via distributors / entrepreneurs mainly based in France and Europe. We want to focus on selling B2C to parents and grandparents, looking to buy presents to their children aged 0 to 10 years old. Those present are educative, unique for each child, and they will learn to have fun and learn to have fun. I would like to redesign our WordPress website https://pebblelanternkids.co.uk/index.php We are a children in the world of books and music books: books, music CDs and DVDs looking for something a little more along the lines of our competitors. See ike www.quillotop.com, www.tavirosa.com, www.lecheminduvelours.com, https://www.lespetitsbrume.com/, https://tinselpaths.com/ Our current website is a bit too old fashioned so I am looking at a much more modern design Here is a link for a few products that are not available here: https://www.filecrate.example/sh/kq417dzopfrnwtb/BXPL3rYmOk2u-sVH4dQkLN-zb?dl=0 We have 2 sides in our website: B2C on the left side and B2B on the right site; B2B is for distributors that are entrepreneurs buying our concept. for the homepage design, the main focus will be B2Consumer Our current page is too blended, lacks reassurance elements and I would like to have a look at this page. from our current stories. here is a link for our business book to give you a feel for it: http://online.pagewavo.com/qtlk/pzme/ MAIN PAGES TO REVIEW / HOMEPAGE / https://pebblelanternkids.co.uk/ BOOKS: https : //pebblelanternkids.co.uk/product-category/personalised-books/ MUSIC: https://pebblelanternkids.co.uk/product-category/music-cds/ BLOG: https://pebblelanternkids.co.uk/blog -2 / Looking forward to seeing you and your questions asap

Target Market(s)

parents and grandparents of children aged 0 to 10 years old. This is for the European market

Industry/Entity Type

Publishing Company

Number of Pages Required

4 page

Colors
0392cd
9bcb3b
ec1f27
757575

Requirements
Must have
• keep within the color code of our RGB logo: D25028 RGB: 8CC364 329BC8 808285
Nice to have
• be more with the style of our competitors. Pebble Lantern Kids am about making children learn the fun way, and develop their morality, self-esteem and confidence. It's about the magic of reading to help children learn while having fun. I have attached visuals but those are just examples and you we encourage you to suggest other ideas

```html
<!DOCTYPE html>
<html lang="en">
<head>
<meta charset="utf-8">
<title>Pebble Lantern Kids – Personalised Storybooks</title>
<link href="https://fonts.googleapis.com/css2?family=Josefin+Sans:wght@400;600;700&family=Open+Sans:wght@400;600;700&family=Roboto+Condensed:wght@400;700&display=swap" rel="stylesheet">
<style>
:root{
  --sky-top:#b9def5;
  --sky-bottom:#e8f5fd;
  --nav:#0b6ec2;
  --nav-active:#1a9ae0;
  --blue:#2e9ad3;
  --blue-dark:#1b6fa8;
  --orange:#f7941d;
  --orange-dark:#e86f0c;
  --green:#6cb33f;
  --green-light:#80c447;
  --green-dark:#579a2c;
  --red:#ec1f27;
  --price:#3aa64a;
  --pale:#eaf6fd;
  --ink:#222;
  --white:#fff;
}
*{box-sizing:border-box;margin:0;padding:0}
html,body{width:1200px;height:3913px;overflow:hidden}
body{position:relative;background:var(--white);font-family:"Open Sans",Arial,sans-serif;color:var(--ink)}
.abs{position:absolute}
.fill{position:absolute}

/* header */
.site-header{left:0;top:0;width:1200px;height:200px;background:linear-gradient(var(--sky-top),var(--sky-bottom))}
.phone{left:92px;top:64px;font-size:24px;font-weight:600;display:flex;align-items:center;gap:16px;color:#222}
.brand{left:548px;top:30px;width:114px;height:114px;border-radius:50%;background:var(--white);border:4px solid var(--orange);display:flex;align-items:center;justify-content:center;text-align:center;font-family:"Josefin Sans",sans-serif;font-weight:700;font-size:16px;line-height:1.15;color:var(--nav);z-index:4}
.cart{left:965px;top:56px;width:136px;height:42px;border:2px solid #9bb;background:var(--white);border-radius:3px;display:flex;align-items:center;justify-content:center;gap:10px;font-size:20px;color:#333}
.main-nav{left:162px;top:170px;width:876px;height:46px;background:var(--nav);display:flex;z-index:3;border-radius:2px;box-shadow:0 2px 6px rgba(0,0,0,.25)}
.main-nav a{color:var(--white);text-decoration:none;font-size:17px;display:flex;align-items:center;justify-content:center;border-right:1px solid rgba(255,255,255,.35)}
.main-nav a.active{background:var(--nav-active)}

/* hero */
.hero{left:0;top:185px;width:1200px;height:600px;overflow:hidden;
  background:
    radial-gradient(ellipse 220px 160px at 300px 230px, rgba(70,140,190,.75), transparent 70%),
    radial-gradient(ellipse 130px 260px at 320px 360px, rgba(60,110,170,.55), transparent 70%),
    radial-gradient(ellipse 170px 120px at 440px 440px, rgba(150,110,70,.9), transparent 72%),
    radial-gradient(ellipse 110px 150px at 780px 410px, rgba(70,160,200,.85), transparent 72%),
    radial-gradient(ellipse 140px 120px at 350px 130px, rgba(120,80,50,.55), transparent 70%),
    linear-gradient(100deg,#b9875a 0%,#dcb68a 40%,#e3c199 60%,#c79c6c 100%)}
.hero-floor{left:0;top:505px;width:1200px;height:95px;background:linear-gradient(#8a5a34,#5a3520)}
.hero-title{left:603px;top:148px;font-family:"Roboto Condensed",sans-serif;color:var(--white);text-shadow:0 2px 4px rgba(0,0,0,.35)}
.hero-title h1{font-size:55px;font-weight:700;line-height:1.1;letter-spacing:-.3px}
.hero-title p{font-size:38px;margin-left:14px;margin-top:2px}
.slider-arrows{left:94px;top:495px;display:flex;gap:16px}
.hero-curve{left:0;top:730px;width:1200px;height:70px}

/* welcome */
.welcome-photo{left:89px;top:887px;width:438px;height:284px;
  background:
    radial-gradient(ellipse 70px 90px at 370px 130px, rgba(80,150,200,.85), transparent 72%),
    radial-gradient(ellipse 110px 80px at 190px 230px, rgba(40,60,110,.55), transparent 72%),
    radial-gradient(ellipse 70px 50px at 190px 70px, rgba(250,250,250,.9), transparent 72%),
    linear-gradient(120deg,#e6dccb,#cfc2ad 60%,#b7a78f)}
.play{left:270px;top:995px;width:68px;height:68px;border-radius:50%;background:rgba(255,255,255,.92)}
.welcome{left:563px;top:902px;width:616px}
.welcome h2{font-family:"Josefin Sans",sans-serif;font-size:33px;font-weight:600;margin-bottom:12px}
.welcome p{font-size:13.5px;line-height:1.72;color:#333;text-align:justify}
.btn{display:inline-flex;align-items:center;justify-content:center;color:var(--white);border-radius:20px;font-size:13px;font-weight:600;text-decoration:none}
.btn-read{margin-top:16px;width:100px;height:32px;background:var(--orange)}

/* tinted band */
.band{left:0;top:1252px;width:1200px;height:1595px;background:var(--pale)}
.band-curve-top{left:0;top:1222px;width:1200px;height:60px}

/* feature cards */
.feature{top:1359px;width:338px;height:300px;color:var(--white);text-align:center;padding-top:100px}
.feature h3{font-family:"Josefin Sans",sans-serif;font-size:22px;font-weight:600;margin-bottom:8px}
.feature p{font-size:13.5px;line-height:1.5;padding:0 40px}
.feature .btn{margin-top:18px;width:144px;height:38px;font-size:14px}
.f-music{left:94px;background:var(--blue)}
.f-books{left:431px;background:linear-gradient(var(--orange),var(--orange-dark))}
.f-dvd{left:768px;background:var(--blue)}
.f-music .btn,.f-dvd .btn{background:var(--blue-dark);border:2px solid rgba(255,255,255,.5)}
.f-books .btn{background:var(--orange-dark);border:2px solid rgba(255,255,255,.5)}
.avatar{top:1258px;width:182px;height:182px;border-radius:50%;border:6px solid;box-shadow:0 2px 6px rgba(0,0,0,.15)}
.av-music{left:172px;border-color:#8ccbec;background:radial-gradient(circle at 50% 45%,#f3c9a3 0 22%,transparent 40%),radial-gradient(circle at 50% 90%,#3f8fd0 0 30%,transparent 50%),linear-gradient(#dfeef7,#bcd8ea)}
.av-books{left:509px;border-color:#f8b76a;background:radial-gradient(circle at 40% 50%,#2f5fa8 0 25%,transparent 45%),radial-gradient(circle at 65% 35%,#e9c6a5 0 18%,transparent 35%),linear-gradient(#f2e3cf,#c9b196)}
.av-dvd{left:846px;border-color:#8ccbec;background:radial-gradient(circle at 50% 42%,#f1cfae 0 22%,transparent 40%),radial-gradient(circle at 50% 88%,#3a70b8 0 28%,transparent 48%),linear-gradient(#e9eef2,#c5d1da)}

/* products */
.section-title{font-family:"Josefin Sans",sans-serif;font-weight:600;font-size:42px;text-align:center;width:1200px;left:0}
.product{width:233px;height:368px;background:var(--white);border:1px solid #ddd;box-shadow:0 1px 4px rgba(0,0,0,.15);text-align:center}
.cover{position:absolute;left:48px;top:26px;width:138px;height:192px;box-shadow:1px 2px 5px rgba(0,0,0,.35)}
.product .name{position:absolute;top:240px;width:100%;font-size:15px}
.product .price{position:absolute;top:268px;width:100%;font-size:15px}
.price s{color:var(--red);margin-right:8px}
.price span{color:var(--price)}
.product .btn{position:absolute;top:298px;left:59px;width:116px;height:26px;background:var(--nav);font-size:12px}
.load-more{left:535px;top:2667px;width:131px;height:42px;border:1px solid #555;background:var(--white);font-size:16px;display:flex;align-items:center;justify-content:center}

/* about */
.about-curve{left:0;top:2815px;width:1200px;height:60px}
.about-col{top:2962px}
.about-col .art{height:160px;margin-bottom:22px}
.about-col h3{font-size:20px;font-weight:600;margin-bottom:8px;text-transform:uppercase}
.about-col h3.plain{text-transform:none}
.about-col p{font-size:13.5px;line-height:1.78;color:#333;font-family:Arial,sans-serif;text-align:justify}
.kids-art{left:425px;top:3312px;width:352px;height:112px;z-index:2;
  background:
    radial-gradient(ellipse 40px 52px at 30px 58px,#f2b24a,transparent 72%),
    radial-gradient(ellipse 40px 52px at 100px 50px,#3d8ad0,transparent 72%),
    radial-gradient(ellipse 40px 52px at 175px 55px,#f3c04a,transparent 72%),
    radial-gradient(ellipse 40px 52px at 250px 55px,#e0574a,transparent 72%),
    radial-gradient(ellipse 40px 52px at 320px 52px,#5fae3e,transparent 72%)}

/* footer */
.site-footer{left:0;top:3360px;width:1200px;height:553px}
.f-col{top:3535px;color:var(--white)}
.f-col h4{font-size:17px;font-weight:400;letter-spacing:.5px;margin-bottom:40px}
.f-col ul{list-style:none;font-size:14px;line-height:32px}
.contact-item{display:flex;gap:12px;font-size:14px;margin-bottom:28px}
.contact-item b{font-weight:400;font-size:15px;display:block}
.f-form input{display:block;width:295px;height:37px;border:1px solid #ccc;margin-bottom:7px;padding:0 12px;font-size:14px;font-family:"Open Sans",sans-serif;color:#333}
.f-form .send{margin-top:8px;width:128px;height:38px;background:var(--blue);color:var(--white);display:flex;align-items:center;justify-content:center;font-size:16px;letter-spacing:.5px}
.f-rule{left:97px;top:3822px;width:1000px;height:1px;background:rgba(255,255,255,.5)}
.copyright{left:0;top:3852px;width:1200px;text-align:center;color:var(--white);font-size:13px}
</style>
</head>
<body>

<header class="abs site-header"></header>
<div class="abs phone">
  <svg width="22" height="22" viewBox="0 0 24 24"><path d="M6.6 10.8a15.2 15.2 0 0 0 6.6 6.6l2.2-2.2a1 1 0 0 1 1-.25 11.4 11.4 0 0 0 3.6.57 1 1 0 0 1 1 1V20a1 1 0 0 1-1 1A17 17 0 0 1 3 4a1 1 0 0 1 1-1h3.5a1 1 0 0 1 1 1c0 1.25.2 2.45.57 3.57a1 1 0 0 1-.25 1z" fill="#333"/></svg>
  555-204-7788
</div>
<div class="abs brand">Pebble<br>Lantern<br>Kids</div>
<div class="abs cart">
  <svg width="22" height="20" viewBox="0 0 24 22"><path d="M1 2h4l3 12h12l3-9H7" fill="none" stroke="#6cb33f" stroke-width="2.2"/><circle cx="10" cy="19" r="2" fill="#6cb33f"/><circle cx="18" cy="19" r="2" fill="#6cb33f"/></svg>
  Cart : 0
</div>
<nav class="abs main-nav">
  <a class="active" style="width:116px" href="#">Home</a>
  <a style="width:142px" href="#">About</a>
  <a style="width:148px" href="#">Product</a>
  <a style="width:200px" href="#">Distributors</a>
  <a style="width:140px" href="#">Blog</a>
  <a style="width:130px;border-right:0" href="#">Contact</a>
</nav>

<section class="abs hero" role="img" aria-label="Photo of a child in an aviator cap and blue scarf standing in a cardboard box beside a personalised activity book">
  <div class="fill hero-floor"></div>
  <div class="fill hero-title"><h1>When Children Become</h1><p>The Heroes Of Their Own Stories</p></div>
  <div class="fill slider-arrows">
    <svg width="14" height="22" viewBox="0 0 14 22"><path d="M11 2 3 11l8 9" stroke="#fff" stroke-width="3" fill="none"/></svg>
    <svg width="14" height="22" viewBox="0 0 14 22"><path d="M3 2l8 9-8 9" stroke="#fff" stroke-width="3" fill="none"/></svg>
  </div>
</section>
<svg class="abs hero-curve" viewBox="0 0 1200 70" preserveAspectRatio="none"><path d="M0 30 Q600 70 1200 30 V70 H0z" fill="#fff"/><path d="M0 30 Q600 70 1200 30" stroke="#2e9ad3" stroke-width="5" fill="none"/></svg>

<div class="abs welcome-photo" role="img" aria-label="Photo of a child in a sailor hat and striped top holding a personalised storybook"></div>
<svg class="abs play" viewBox="0 0 68 68"><path d="M27 21l20 13-20 13z" fill="#333"/></svg>
<section class="abs welcome">
  <h2>Welcome to Pebble Lantern Kids</h2>
  <p>It is a long established fact that a reader will be distracted by the readable content of a page when looking at its layout. The point of using Lorem Ipsum is that it has a more-or-less normal distribution of letters, as opposed to using 'Content here, content here', making it look like readable English Many desktop publishing packages and web page editors now use Lorem Ipsum as their default model text, and a search for 'lorem ipsum' will uncover many web sites still in their infancy.</p>
  <a class="btn btn-read" href="#">Read More</a>
</section>

<div class="abs band"></div>
<svg class="abs band-curve-top" viewBox="0 0 1200 60" preserveAspectRatio="none"><path d="M0 40 Q600 0 1200 40 V60 H0z" fill="#eaf6fd"/></svg>

<div class="abs feature f-music"><h3>Music</h3><p>It is a long established fact that a reader will be distracted by the readable content of a page when looking</p><a class="btn" href="#">View More</a></div>
<div class="abs feature f-books"><h3>Personalised books</h3><p>It is a long established fact that a reader will be distracted by the readable content of a page when looking</p><a class="btn" href="#">View More</a></div>
<div class="abs feature f-dvd"><h3>DVD cartoon</h3><p>It is a long established fact that a reader will be distracted by the readable content of a page when looking</p><a class="btn" href="#">View More</a></div>
<div class="abs avatar av-music" role="img" aria-label="Photo of a child wearing headphones"></div>
<div class="abs avatar av-books" role="img" aria-label="Photo of a grandparent reading a book with a child"></div>
<div class="abs avatar av-dvd" role="img" aria-label="Photo of a child watching a cartoon"></div>

<h2 class="abs section-title" style="top:1745px">Our Products</h2>

<div class="abs product" style="left:89px;top:1845px"><div class="cover" style="background:linear-gradient(#f7d35a 0%,#f2a94a 35%,#9ccf63 70%,#5ea83c 100%)" role="img" aria-label="Book cover: a day on the farm"></div><div class="name">Product Name</div><div class="price"><s>$179</s><span>$145.65</span></div><a class="btn" href="#">Add to Cart</a></div>
<div class="abs product" style="left:347px;top:1845px"><div class="cover" style="background:linear-gradient(#a9dcf0 0%,#c7e6f3 30%,#9a7fd0 65%,#6aa545 100%)" role="img" aria-label="Book cover: the mysterious dragon"></div><div class="name">Product Name</div><div class="price"><s>$179</s><span>$145.65</span></div><a class="btn" href="#">Add to Cart</a></div>
<div class="abs product" style="left:605px;top:1845px"><div class="cover" style="background:linear-gradient(#f6cf52 0%,#f0b13c 30%,#92c24c 65%,#4f8f2e 100%)" role="img" aria-label="Book cover: dinosaur story"></div><div class="name">Product Name</div><div class="price"><s>$179</s><span>$145.65</span></div><a class="btn" href="#">Add to Cart</a></div>
<div class="abs product" style="left:861px;top:1845px"><div class="cover" style="background:linear-gradient(#203f8c 0%,#3d64b5 30%,#e4e8ef 55%,#d7382f 100%)" role="img" aria-label="Book cover: Christmas story"></div><div class="name">Product Name</div><div class="price"><s>$179</s><span>$145.65</span></div><a class="btn" href="#">Add to Cart</a></div>

<div class="abs product" style="left:89px;top:2260px"><div class="cover" style="background:linear-gradient(#e23c34 0%,#f07a3a 35%,#f5c24a 65%,#8ac350 100%)" role="img" aria-label="Book cover: fairy queen story"></div><div class="name">Product Name</div><div class="price"><s>$179</s><span>$145.65</span></div><a class="btn" href="#">Add to Cart</a></div>
<div class="abs product" style="left:347px;top:2260px"><div class="cover" style="background:linear-gradient(#0b1220 0%,#15243e 45%,#2f7a48 80%,#4fa45a 100%)" role="img" aria-label="Book cover: superheroes in space"></div><div class="name">Product Name</div><div class="price"><s>$179</s><span>$145.65</span></div><a class="btn" href="#">Add to Cart</a></div>
<div class="abs product" style="left:605px;top:2260px"><div class="cover" style="background:linear-gradient(#8fd0ec 0%,#5cb2de 35%,#e6c98e 65%,#3a7ec0 100%)" role="img" aria-label="Book cover: treasure island adventure"></div><div class="name">Product Name</div><div class="price"><s>$179</s><span>$145.65</span></div><a class="btn" href="#">Add to Cart</a></div>
<div class="abs product" style="left:861px;top:2260px"><div class="cover" style="background:linear-gradient(#3c2460 0%,#5d3488 40%,#8f4aa0 70%,#5aa34a 100%)" role="img" aria-label="Book cover: trip into space"></div><div class="name">Product Name</div><div class="price"><s>$179</s><span>$145.65</span></div><a class="btn" href="#">Add to Cart</a></div>

<div class="abs load-more">Load More</div>

<svg class="abs about-curve" viewBox="0 0 1200 60" preserveAspectRatio="none"><path d="M0 40 Q600 0 1200 40 V60 H0z" fill="#fff"/></svg>
<h2 class="abs section-title" style="top:2890px">About us</h2>

<div class="abs about-col" style="left:117px;width:250px"><div class="art" style="width:125px;background:radial-gradient(ellipse 48% 50% at 50% 50%,#f5b23a 55%,rgba(245,178,58,0) 100%)" role="img" aria-label="Illustration of a yellow cartoon dinosaur"></div><h3>Our Vision</h3><p>Is to make children the heroes of the adventure and live magical and unforgettable moments they can share with their family and friends.</p></div>
<div class="abs about-col" style="left:480px;width:252px"><div class="art" style="width:175px;background:radial-gradient(ellipse 50% 35% at 50% 55%,#77bb45 55%,rgba(119,187,69,0) 100%)" role="img" aria-label="Illustration of a green cartoon stegosaurus"></div><h3>Our Mission</h3><p>Personalisation offers for children to have an opportunity to recognise themselves in the story, thus developing the morale, self-esteem and confidence.</p></div>
<div class="abs about-col" style="left:837px;width:260px"><div class="art" style="width:140px;background:radial-gradient(ellipse 48% 42% at 50% 50%,#8a6fc4 55%,rgba(138,111,196,0) 100%)" role="img" aria-label="Illustration of a purple cartoon dragon"></div><h3 class="plain">Distributors</h3><p>All our stories aim to stimulate learning and enhance reading passion from an early age and have been designed with high-quality original artwork</p></div>

<svg class="abs site-footer" viewBox="0 0 1200 553" preserveAspectRatio="none"><defs><linearGradient id="grass" x1="0" y1="0" x2="0" y2="1"><stop offset="0" stop-color="#80c447"/><stop offset="1" stop-color="#5c9f31"/></linearGradient></defs><path d="M0 45 Q600 -25 1200 45 V553 H0z" fill="url(#grass)"/></svg>
<div class="abs kids-art" role="img" aria-label="Illustration of a group of cartoon children jumping"></div>

<div class="abs f-col" style="left:97px">
  <h4>CONTACT US</h4>
  <div class="contact-item"><svg width="22" height="16" viewBox="0 0 22 16"><rect x="1" y="1" width="20" height="14" fill="none" stroke="#fff" stroke-width="1.6"/><path d="M1 1l10 8 10-8" fill="none" stroke="#fff" stroke-width="1.6"/></svg><div><b>EMAIL ADDRESS</b>hello@pebblelanternkids.co.uk</div></div>
  <div class="contact-item"><svg width="22" height="22" viewBox="0 0 24 24"><path d="M6.6 10.8a15.2 15.2 0 0 0 6.6 6.6l2.2-2.2a1 1 0 0 1 1-.25 11.4 11.4 0 0 0 3.6.57 1 1 0 0 1 1 1V20a1 1 0 0 1-1 1A17 17 0 0 1 3 4a1 1 0 0 1 1-1h3.5a1 1 0 0 1 1 1c0 1.25.2 2.45.57 3.57a1 1 0 0 1-.25 1z" fill="none" stroke="#fff" stroke-width="1.5"/></svg><div><b>PHONE NUMBER</b>0400 118 263</div></div>
</div>
<div class="abs f-col" style="left:384px"><h4>LINKS</h4><ul><li>Home</li><li>About Us</li><li>Support Center</li><li>Product</li></ul></div>
<div class="abs f-col" style="left:587px"><h4>RESOURCES</h4><ul><li>Distributors</li><li>Features</li><li>Blog</li><li>Contact Us</li></ul></div>
<div class="abs f-col f-form" style="left:799px">
  <h4 style="margin-bottom:24px">GET IN TOUCH</h4>
  <input type="text" placeholder="Your Name">
  <input type="text" placeholder="Email address">
  <input type="text" placeholder="Phone">
  <div class="send">SEND</div>
</div>
<div class="abs f-rule"></div>
<p class="abs copyright">© Copyright 2018 . All Rights Reserved. Terms and Conditions | Privacy Policy</p>

</body>
</html>
```